Coffeeshop menu for filter tip

We want to have a cannabis (coffeeshop) menu in the size 25mm wide x 60mm wide. Some examples attached.

it must have the following text:
Menu

WEED p/g
Velotrine €16
Cinderfox €14
Tide Rambler €14
Marigolden €16
Grand Pelican €14
Copper Comet €14

HASH p/g
Baltic Ember €12
Harbor Velvet€11
Plum Rova €14
Dusk Maple €10

Target Market(s)

tourist in Amsterdam

Requirements
Nice to have
• cannabis sign leaf
• No Cigarettes allowed symbol

```html
<!DOCTYPE html>
<html lang="en">
<head>
<meta charset="utf-8">
<title>Amsterdam Menu</title>
<link rel="stylesheet" href="https://fonts.googleapis.com/css2?family=Cinzel:wght@400;500&family=Caudex:wght@400;700&display=swap">
<style>
  :root {
    --bg-dark: #330a0d;
    --bg-red: #5c0d10;
    --bg-warm: #7a3a28;
    --frame: #9a5128;
    --rule: #8a4524;
    --rule-faint: #5a1a14;
    --ink: #ffffff;
    --cup: #c9a6a3;
    --leaf: rgba(190, 150, 150, 0.45);
    --sign-red: #e3141e;
    --smoke: #ffffff;
  }
  html, body {
    margin: 0;
    padding: 0;
    width: 1200px;
    height: 2871px;
    overflow: hidden;
    background: var(--bg-dark);
  }
  .menu-card {
    display: block;
    width: 1200px;
    height: 2871px;
  }
  .menu-title {
    font-family: "Cinzel", serif;
    font-weight: 500;
    fill: var(--ink);
    font-size: 112px;
    text-anchor: middle;
  }
  .section-head {
    font-family: "Caudex", serif;
    font-weight: 400;
    fill: var(--ink);
    font-size: 92px;
  }
  .item-name, .item-price {
    font-family: "Caudex", serif;
    font-weight: 700;
    fill: var(--ink);
    font-size: 72px;
  }
  .item-price, .unit { text-anchor: end; }
</style>
</head>
<body>
<svg class="menu-card" viewBox="0 0 1200 2871" xmlns="http://www.w3.org/2000/svg">
  <defs>
    <linearGradient id="card-bg" x1="1" y1="0" x2="0" y2="1">
      <stop offset="0" stop-color="var(--bg-dark)"/>
      <stop offset="0.55" stop-color="var(--bg-red)"/>
      <stop offset="1" stop-color="var(--bg-warm)"/>
    </linearGradient>
    <radialGradient id="leaf-glow" cx="0.5" cy="0.5" r="0.5">
      <stop offset="0" stop-color="rgba(190,150,150,0.35)"/>
      <stop offset="1" stop-color="rgba(190,150,150,0)"/>
    </radialGradient>
  </defs>

  <!-- background and frame -->
  <rect class="card-bg" x="0" y="0" width="1200" height="2871" fill="url(#card-bg)"/>
  <rect class="card-frame" x="31" y="31" width="1138" height="2809" fill="none" stroke="var(--frame)" stroke-width="12"/>

  <!-- coffee cup icon -->
  <g class="cup-icon" fill="var(--cup)">
    <path d="M120 152 q-18 18 0 36 q18 18 0 36" fill="none" stroke="var(--cup)" stroke-width="9" stroke-linecap="round"/>
    <path d="M152 140 q-18 18 0 36 q18 18 0 36" fill="none" stroke="var(--cup)" stroke-width="9" stroke-linecap="round"/>
    <path d="M184 152 q-18 18 0 36 q18 18 0 36" fill="none" stroke="var(--cup)" stroke-width="9" stroke-linecap="round"/>
    <path d="M78 238 h160 v60 q0 50 -50 60 h-60 q-50 -10 -50 -60 z"/>
    <path d="M236 256 q52 0 48 34 q-4 34 -56 40" fill="none" stroke="var(--cup)" stroke-width="14"/>
    <rect x="58" y="356" width="210" height="16" rx="8"/>
  </g>

  <text class="menu-title" x="604" y="180">Amsterdam</text>
  <text class="menu-title" x="600" y="377">Menu</text>
  <rect class="title-rule" x="66" y="403" width="1046" height="5" fill="var(--rule)"/>

  <!-- faint leaf decoration area -->
  <rect class="leaf-mark" x="350" y="1086" width="710" height="771" fill="url(#leaf-glow)" role="img" aria-label="Faint cannabis leaf decoration"/>

  <!-- weed section -->
  <text class="section-head" x="102" y="640">WEED</text>
  <text class="section-head unit" x="1025" y="640">p/g</text>
  <rect class="section-rule" x="66" y="673" width="1046" height="3" fill="var(--rule-faint)"/>

  <g class="price-list weed-list">
    <text class="item-name" x="84" y="792">Velotrine</text><text class="item-price" x="1025" y="792">€16</text>
    <text class="item-name" x="84" y="955">Cinderfox</text><text class="item-price" x="1018" y="955">€14</text>
    <text class="item-name" x="84" y="1116">Tide Rambler</text><text class="item-price" x="1018" y="1116">€14</text>
    <text class="item-name" x="84" y="1279">Marigolden</text><text class="item-price" x="1013" y="1279">€16</text>
    <text class="item-name" x="84" y="1440">Grand Pelican</text><text class="item-price" x="1018" y="1440">€14</text>
    <text class="item-name" x="84" y="1603">Copper Comet</text><text class="item-price" x="1028" y="1603">€14</text>
  </g>

  <!-- hash section -->
  <text class="section-head" x="84" y="1862">HASH</text>
  <text class="section-head unit" x="1042" y="1862">p/g</text>
  <rect class="section-rule" x="66" y="1894" width="1046" height="6" fill="var(--rule)"/>

  <g class="price-list hash-list">
    <text class="item-name" x="82" y="2024">Baltic Ember</text><text class="item-price" x="1046" y="2024">€12</text>
    <text class="item-name" x="82" y="2186">Harbor Velvet</text><text class="item-price" x="1051" y="2186">€11</text>
    <text class="item-name" x="82" y="2348">Plum Rova</text><text class="item-price" x="1056" y="2348">€14</text>
    <text class="item-name" x="82" y="2509">Dusk Maple</text><text class="item-price" x="1053" y="2509">€10</text>
  </g>

  <!-- no smoking sign -->
  <g class="no-smoking">
    <rect x="152" y="2706" width="50" height="20" fill="#a0683e"/>
    <rect x="202" y="2706" width="110" height="20" fill="var(--smoke)"/>
    <path d="M322 2704 q10 -40 50 -50 q30 -8 28 -30 M330 2700 q20 -30 54 -34" fill="none" stroke="var(--smoke)" stroke-width="4" stroke-linecap="round"/>
    <circle cx="233" cy="2716" r="60" fill="none" stroke="var(--sign-red)" stroke-width="12"/>
    <line x1="190" y1="2673" x2="276" y2="2759" stroke="var(--sign-red)" stroke-width="12"/>
  </g>
</svg>
</body>
</html>
```